Label for Skincare Brand

"Fernleigh Vale Organics" - organic skincare brand
I need a label designed for my organic skincare brand. I have attached pics of brands I like, to give you an idea of style. I would like something minimal although some colour might work. Colours I like are pale blush pink and aqua. I would like a clean, minimalistic modern yet elegant label. Please look at the samples because they demonstrate the style I look for in a label. It is okay to add a graphical element into the design as long as it enhances or add value to the design.
We do not have a logo yet, so I'd appreciate if you could create a simple type logo for Fernleigh Vale Organics similar to the examples attached.
Please can you do two different sizes: one cream jar and one serum bottle. Both will contain the same information.
___________________________________________________
1. Cream Jar (label size 42 x 190 mm) (clear glass with aluminium lid)
2. Serum Bottle (label size 50 x 110 mm) (clear glass with black pump)
FRONT SIDE:
Fernleigh Vale Organics
Nine Moons
Ultimate Anti-Aging Cream
For Dry & Mature Skin
Organic & Palm Oil-Free
100 ml.
BACK SIDE:
Nine Moons Ultimate Anti-Aging Cream
An effective Day Cream that harnesses the best of science to target the signs of aging. The main active ingredient is R58, a patented noncomedogenic lipid complex, carefully engineered from botanically-sourced lipids. It is composed of a variety of lipid types which are carefully combined in the same ratio as those found on healthy young skin of an average 22 year old.
Directions:
Apply to clean skin morning and night.
Ingredients:
Aloe Vera Leaf Juice, Cocos Nucifera Oil, Butyrospermum Parkii Butter, Jojoba Oil/Macadamia Seed Oil Esters (and) Squalene (and) Phytosteryl Macadamiate (and) Phytosterols, Potassium Olivoyl Hydrolyzed Oat Protein (and) Cetearyl Alcohol (and) Glyceryl Oleate (and) Glyceryl Stearat, Benzyl Alcohol, Dehydroacetic Acid.
Fernleigh Vale Organics
6/3 Kelmora Street North, Wahroonga, NSW 2076
www.fernleighvaleorganics.com.au
Any questions, please just ask away. Thank you.

```html
<!DOCTYPE html>
<html lang="en">
<head>
<meta charset="utf-8">
<title>Fernleigh Vale Organics – Nine Moons Cream Label</title>
<link rel="stylesheet" href="https://fonts.googleapis.com/css2?family=Jost:wght@300;400;500&display=swap">
<style>
  :root {
    --backdrop: #808080;
    --label: #ffffff;
    --blush: #f0bdc8;
    --brand-grey: #555557;
    --ink: #3a3a3c;
  }
  html, body {
    margin: 0;
    padding: 0;
    width: 1200px;
    height: 2306px;
    overflow: hidden;
    background: var(--backdrop);
  }
  .label {
    position: absolute;
    left: 83px;
    top: 81px;
    width: 1034px;
    height: 2141px;
    background: var(--label);
    font-family: "Jost", "Futura", sans-serif;
  }
  .blush-band {
    position: absolute;
    left: 58px;
    top: 58px;
    width: 918px;
    height: 155px;
    background: var(--blush);
  }
  .line {
    position: absolute;
    left: 0;
    width: 100%;
    margin: 0;
    text-align: center;
    line-height: 1;
    white-space: nowrap;
  }
  .brand-name {
    top: 470px;
    font-size: 72px;
    font-weight: 400;
    color: var(--brand-grey);
  }
  .brand-name span { display: block; height: 82px; }
  .product-name {
    top: 775px;
    font-size: 58px;
    font-weight: 300;
    color: var(--ink);
  }
  .product-name span { display: block; height: 66px; }
  .product-title {
    top: 1058px;
    font-size: 104px;
    font-weight: 500;
    color: var(--ink);
  }
  .claims {
    top: 1316px;
    font-size: 52px;
    font-weight: 300;
    color: var(--ink);
  }
  .claims span { display: block; height: 59px; }
  .volume {
    top: 1894px;
    font-size: 48px;
    font-weight: 300;
    color: var(--ink);
  }
</style>
</head>
<body>
  <main class="label">
    <div class="blush-band"></div>

    <p class="line brand-name">
      <span>FERNLEIGH VALE</span>
      <span>ORGANICS</span>
    </p>

    <p class="line product-name">
      <span>ULTIMATE</span>
      <span>ANTI-AGING</span>
      <span>CREAM</span>
    </p>

    <h1 class="line product-title">NINE MOONS</h1>

    <p class="line claims">
      <span>For Dry &amp; Mature Skin</span>
      <span>Organic &amp; Palm Oil-Free</span>
    </p>

    <p class="line volume">100mL</p>
  </main>
</body>
</html>
```